Web design for a pet services marketplace

I represent a South American based company: “TORVELIS” which provides a different array of pet related services. As a starting point, I would like to get proposals for 1 page website (plus a general frame for forms, instructions etc) web design job for a dog boarding marketplace. If you could add a logo is desirable.
By a Dog Boarding Marketplace, I mean a community marketplace, very much like an roomswap, but for pet services (initially dog boarding/daycare, but evolving to other services such as dog walkers. The purpose is to bring together dog owners and dog-care providers according to qualifications or characteristics given at time of input and needs of the dog owner given at the time of searching. Providers create a profile, entering certain information requested in forms such as their location, type of house/apt, what type/size of dogs they take, prior experience, as well as a personal introduction and pictures. Providers will set their own rates and calendar availability. Then customers browse, schedule and book and pay online. As it works for similar services, there will be a system of reviews and feedback for each care provider.
As to the website, it should be substantially similar to the following websites: (www.pupstayo.com , www.kelbo.com). It should be simple and straightforward, prioritizing ease of use. I would like for visitors to easily understand how the model works by seeing the home page, and getting pop up explanations by browsing over each main icon or message on the homepage. Therefore, I would try to keep additional pages to a minimum.
As I’m new to this, I would not venture as to how many pages I would need and would defer to your suggestion, according to the examples provided. However, I would like to have a visually striking front end, with dog related pictures or cartoon type images. Icons etc should be fun, and related to dogs, vacations, hotels/lodging, travel, etc. Secondary pages (like enrollment forms, Q&A, etc) could have a clean design, maybe adding some non-obtrusive related imagery.
Please note that attached pictures are , third party property and are for guide only.
Additional info:
In general I want to make a site very much like the examples of pupstayo and kelbo, but i think a better job could be done in terms of design. Please feel free to provide your own ideas.
1. For now, since the site will be new, we would not be including a testimonials section. However, we could use the space , or maybe smaller, with the "spread the love"section for announcing special deals for people who share the project.
2. In the principal section, I would like to see a clean layout. Much like pupstayo does. As an alternative, I would also like to see how it would look like if we handled more cartoon type drawings instead of pictures (just a suggestion to see how it would look like).
3. Search spaces should be more floating (merging more with background), as in pupstayo, not in larger boxes.
Updates
Please find in the attachments a very rough wire frame that i just did as response to a project proposal. Please note where i say OK (top and bottom) I mean that those two sections i found ok in such project or the model websites. Pretty regular content in those sections. Added Friday, July 10, 2015
Target Market(s)
dog owners, people who are willing to host pets in their home, kennels
Industry/Entity Type
Pet Care
Number of Pages Required
1 page
Look and feel

```html
<!DOCTYPE html>
<html lang="en">
<head>
<meta charset="utf-8">
<title>TORVELIS – Find a loving Dog Sister</title>
<link rel="stylesheet" href="https://fonts.googleapis.com/css2?family=Open+Sans:ital,wght@0,300;0,400;0,600;0,700;1,700&display=swap">
<style>
  :root{
    --green:#6cbf4b;
    --green-head:#5fb843;
    --green-dark:#3f8a2c;
    --green-band:#7cc55c;
    --green-pale:#e8f4e1;
    --orange:#f4a64a;
    --text:#4a4a4a;
    --muted:#8a8a8a;
    --line:#dcdcdc;
    --white:#ffffff;
  }
  *{box-sizing:border-box;margin:0;padding:0}
  html,body{width:1200px;height:2960px;overflow:hidden}
  body{font-family:"Open Sans",Arial,sans-serif;color:var(--text);background:var(--white);position:relative}
  .abs{position:absolute}

  /* header */
  .site-header{position:absolute;left:0;top:0;width:1200px;height:64px;background:rgba(108,191,75,.95);z-index:2;display:flex;align-items:center;padding:0 40px}
  .brand{display:flex;align-items:center;gap:8px;background:var(--white);padding:6px 12px;border-radius:3px}
  .brand-dot{width:14px;height:14px;border-radius:50%;background:var(--green)}
  .brand-name{font-weight:700;font-size:15px;color:var(--green-dark)}
  .main-nav{display:flex;gap:44px;margin-left:60px;font-size:14px;color:var(--white)}
  .account-nav{margin-left:auto;display:flex;align-items:center;gap:40px;font-size:14px;color:var(--white)}
  .btn-outline{border:1.5px solid var(--white);padding:7px 22px;border-radius:3px}

  /* hero */
  .hero{position:absolute;left:0;top:0;width:1200px;height:532px;overflow:hidden}
  .hero-photo{position:absolute;inset:0;
    background:
      radial-gradient(ellipse 170px 230px at 1010px 330px,#3a3d33 0%,#4a4c40 45%,rgba(74,76,64,0) 100%),
      radial-gradient(ellipse 90px 80px at 960px 150px,#3b2a20 0%,rgba(59,42,32,0) 100%),
      radial-gradient(ellipse 230px 70px at 640px 440px,#c58b55 0%,#e6c9a6 50%,rgba(230,201,166,0) 100%),
      radial-gradient(ellipse 160px 60px at 880px 480px,#d7a877 0%,rgba(215,168,119,0) 100%),
      linear-gradient(180deg,#f6f5f1 0%,#eeeae3 60%,#e2d9cc 100%)}
  .hero-title{left:90px;top:122px;font-size:44px;font-weight:300;color:#555}
  .hero-sub{left:92px;top:182px;font-size:17px;color:#666}
  .search-row{left:88px;top:242px;display:flex}
  .search-input{width:332px;height:38px;background:rgba(255,255,255,.85);border:1px solid var(--line);font-size:14px;color:var(--muted);padding:9px 14px}
  .search-btn{width:120px;height:38px;background:var(--green);color:var(--white);font-size:14px;display:flex;align-items:center;justify-content:center}
  .date-row{left:88px;top:294px;display:flex;gap:14px}
  .date-field{width:100px;height:30px;border:1px solid var(--line);background:rgba(255,255,255,.85);font-size:12px;color:var(--muted);display:flex;align-items:center;gap:6px;padding:0 10px}
  .date-field i{width:10px;height:10px;border-radius:50%;border:1.5px solid var(--green);display:block}
  .size-row{left:88px;top:342px;display:flex;gap:14px}
  .size-btn{width:80px;height:30px;font-size:12px;color:var(--white);display:flex;align-items:center;justify-content:center;border-radius:2px}
  .size-btn.small{background:var(--green)}
  .size-btn.large{background:var(--orange)}

  /* section headings */
  .section-title{font-weight:300;color:var(--green-head);font-size:58px}

  /* how it works */
  .step-heading{display:flex;align-items:center;gap:10px;font-size:42px;font-weight:600;color:var(--green-head);line-height:52px}
  .step-text{font-size:15px;line-height:21px;color:#555;width:380px}

  /* features */
  .feature{position:absolute;top:1440px;width:300px;text-align:center}
  .feature-icon{height:150px;display:flex;align-items:center;justify-content:center}
  .feature-name{font-size:30px;font-weight:300;color:var(--green-head);margin-top:18px}
  .feature-text{font-size:15px;line-height:21px;color:#555;margin:10px auto 0;width:250px}
  .feature-divider{position:absolute;top:1450px;width:1px;height:320px;background:var(--line)}

  /* testimonial */
  .testimonial-panel{left:150px;top:1925px;width:900px;height:370px;border:1px solid var(--line);box-shadow:0 2px 6px rgba(0,0,0,.12);border-radius:4px}
  .avatar{width:78px;height:78px;border-radius:50%}
  .quote-box{border:1px solid var(--line);border-radius:4px;padding:14px 18px;font-size:12.5px;line-height:18px;color:#666;width:620px;background:var(--white)}
  .author{font-size:11px;color:var(--green-head);text-align:center;line-height:15px;width:110px}

  /* newsletter */
  .newsletter{left:0;top:2360px;width:1200px;height:250px;background:var(--green-band)}
  .newsletter-title{position:absolute;top:52px;width:1200px;text-align:center;font-style:italic;font-weight:700;font-size:28px;color:var(--white)}
  .newsletter-form{position:absolute;left:276px;top:118px;display:flex}
  .newsletter-input{width:530px;height:60px;background:var(--white);font-size:17px;color:var(--muted);padding:18px 20px}
  .newsletter-btn{width:130px;height:60px;background:var(--green-dark);color:var(--white);font-size:19px;display:flex;align-items:center;justify-content:center}

  /* footer */
  .footer-col{position:absolute;top:2650px;font-size:13px;line-height:19px;color:#777}
  .footer-col h4{font-size:18px;font-weight:600;color:#555;margin-bottom:6px}
  .footer-col h4.spaced{margin-top:16px}
  .footer-small-title{font-size:13px;font-weight:600;color:#555;margin-bottom:8px}
  .keep-form{display:flex;margin-bottom:26px}
  .keep-input{width:150px;height:26px;border:1px solid var(--line);font-size:11px;color:var(--muted);padding:5px 8px}
  .keep-btn{width:48px;height:26px;background:var(--green);color:var(--white);font-size:12px;display:flex;align-items:center;justify-content:center;margin-left:8px}
  .social-list{display:flex;gap:10px}
  .social-list span{width:38px;height:38px;border-radius:50%;border:2px solid var(--green);display:block}
  .footer-deco{left:890px;top:2690px;width:310px;height:270px;background:radial-gradient(circle at 60% 60%,var(--green-pale) 0%,rgba(232,244,225,.5) 55%,rgba(255,255,255,0) 75%)}
</style>
</head>
<body>

<section class="hero">
  <div class="hero-photo" role="img" aria-label="Photo of a woman kneeling in a bright living room, feeding small dogs from bowls on the floor"></div>
  <h1 class="abs hero-title">Find a loving Dog Sister</h1>
  <p class="abs hero-sub">Search thousands of trusted, insured pet sitters near you</p>
  <div class="abs search-row">
    <div class="search-input">City or zip</div>
    <div class="search-btn">Find a Sister</div>
  </div>
  <div class="abs date-row">
    <div class="date-field"><i></i>Start date</div>
    <div class="date-field"><i></i>End date</div>
  </div>
  <div class="abs size-row">
    <div class="size-btn small">Small dog</div>
    <div class="size-btn large">Large dog</div>
  </div>
</section>

<header class="site-header">
  <div class="brand"><span class="brand-dot"></span><span class="brand-name">TORVELIS</span></div>
  <nav class="main-nav"><span>Find a Sister</span><span>How it works</span></nav>
  <nav class="account-nav"><span>Login</span><span>Signup</span><span class="btn-outline">Become a Sister</span></nav>
</header>

<h2 class="abs section-title" style="left:70px;top:555px">How it works</h2>

<!-- Search -->
<div class="abs" style="left:160px;top:660px;width:260px;height:200px;background:radial-gradient(ellipse 120px 95px at 50% 52%,#c49a72 0%,#e7d2bb 45%,#f6efe7 75%,rgba(255,255,255,0) 100%)" role="img" aria-label="Smiling woman lying down hugging a small white dog"></div>
<div class="abs" style="left:432px;top:680px">
  <div class="step-heading">
    <svg width="36" height="36" viewBox="0 0 36 36" fill="#5fb843"><ellipse cx="18" cy="24" rx="9" ry="8"/><circle cx="7" cy="14" r="4"/><circle cx="14" cy="7" r="4"/><circle cx="22" cy="7" r="4"/><circle cx="29" cy="14" r="4"/></svg>
    Search
  </div>
  <p class="step-text">Lorem ipsum dolor sit amet, consectetur adipiscing elit, sed do eiusmod tempor incididunt ut labore et dolore magna aliqua. Ut enim ad minim veniam, quis nostrud exercitation ullamco laboris nisi ut aliquip ex ea commodo consequat.</p>
</div>

<!-- Book -->
<div class="abs" style="left:280px;top:905px">
  <div class="step-heading">
    <svg width="36" height="36" viewBox="0 0 36 36" fill="#5fb843"><ellipse cx="18" cy="24" rx="9" ry="8"/><circle cx="7" cy="14" r="4"/><circle cx="14" cy="7" r="4"/><circle cx="22" cy="7" r="4"/><circle cx="29" cy="14" r="4"/></svg>
    Book
  </div>
  <p class="step-text" style="width:380px">Lorem ipsum dolor sit amet, consectetur adipiscing elit, sed do eiusmod tempor incididunt ut labore et dolore magna aliqua. Ut enim ad minim veniam, quis nostrud exercitation ullamco laboris nisi ut aliquip ex ea commodo consequat.</p>
</div>
<div class="abs" style="left:780px;top:845px;width:280px;height:215px;background:radial-gradient(ellipse 125px 95px at 50% 55%,#b9804e 0%,#e3c7a6 40%,#f7f1ea 72%,rgba(255,255,255,0) 100%)" role="img" aria-label="Small white and tan terrier puppy lying down"></div>

<!-- Relax -->
<div class="abs" style="left:210px;top:1095px;width:280px;height:215px;background:radial-gradient(ellipse 125px 100px at 50% 52%,#6e4b30 0%,#a47a55 45%,#e2cdb6 75%,rgba(255,255,255,0) 100%)" role="img" aria-label="White puppy resting inside a brown plush dog house"></div>
<div class="abs" style="left:512px;top:1120px">
  <div class="step-heading">
    <svg width="36" height="36" viewBox="0 0 36 36" fill="#5fb843"><ellipse cx="18" cy="24" rx="9" ry="8"/><circle cx="7" cy="14" r="4"/><circle cx="14" cy="7" r="4"/><circle cx="22" cy="7" r="4"/><circle cx="29" cy="14" r="4"/></svg>
    Relax
  </div>
  <p class="step-text">Lorem ipsum dolor sit amet, consectetur adipiscing elit, sed do eiusmod tempor incididunt ut labore et dolore magna aliqua. Ut enim ad minim veniam, quis nostrud exercitation ullamco laboris nisi ut aliquip ex ea commodo consequat.</p>
</div>

<!-- Features -->
<h2 class="abs section-title" style="left:0;width:1200px;text-align:center;top:1340px">Features</h2>

<div class="feature" style="left:120px">
  <div class="feature-icon">
    <svg width="140" height="140" viewBox="0 0 140 140" fill="none" stroke="#5fb843" stroke-width="4">
      <circle cx="70" cy="66" r="38"/>
      <path d="M30 100 Q12 70 26 36" />
      <path d="M110 100 Q128 70 114 36" />
      <path d="M50 122 L70 108 L90 122" />
      <path d="M58 66 L66 74 L84 56" stroke-width="6"/>
    </svg>
  </div>
  <div class="feature-name">Insured Pets</div>
  <p class="feature-text">Lorem ipsum dolor sit amet, consectetur adipiscing elit, sed do eiusmod tempor incididunt ut labore et dolore magna aliqua.</p>
</div>
<div class="feature-divider" style="left:420px"></div>

<div class="feature" style="left:450px">
  <div class="feature-icon">
    <svg width="120" height="120" viewBox="0 0 120 120">
      <rect x="10" y="10" width="100" height="100" rx="6" fill="#5fb843"/>
      <rect x="24" y="30" width="72" height="58" rx="4" fill="none" stroke="#fff" stroke-width="4"/>
      <circle cx="46" cy="52" r="8" fill="#fff"/>
      <path d="M32 78 Q46 62 60 78 Z" fill="#fff"/>
      <rect x="66" y="46" width="22" height="4" fill="#fff"/>
      <rect x="66" y="58" width="22" height="4" fill="#fff"/>
      <rect x="66" y="70" width="16" height="4" fill="#fff"/>
    </svg>
  </div>
  <div class="feature-name">Vetted Host</div>
  <p class="feature-text">Lorem ipsum dolor sit amet, consectetur adipiscing elit, sed do eiusmod tempor incididunt ut labore et dolore magna aliqua.</p>
</div>
<div class="feature-divider" style="left:780px"></div>

<div class="feature" style="left:780px">
  <div class="feature-icon">
    <svg width="120" height="120" viewBox="0 0 120 120">
      <path d="M60 10 L112 56 L98 56 L98 110 L22 110 L22 56 L8 56 Z" fill="#5fb843"/>
      <path d="M44 110 L44 78 Q60 62 76 78 L76 110 Z" fill="#fff"/>
    </svg>
  </div>
  <div class="feature-name">One on One TLC</div>
  <p class="feature-text">Lorem ipsum dolor sit amet, consectetur adipiscing elit, sed do eiusmod tempor incididunt ut labore et dolore magna aliqua.</p>
</div>

<!-- Testimonial -->
<h2 class="abs section-title" style="left:0;width:1200px;text-align:center;top:1835px;font-size:50px">Testimonial</h2>
<div class="abs testimonial-panel"></div>

<div class="abs avatar" style="left:190px;top:1960px;background:radial-gradient(circle at 50% 45%,#c79d73 0%,#e4cfb4 55%,#a9825e 100%)" role="img" aria-label="Round portrait of a dog owner holding her dog"></div>
<div class="abs author" style="left:174px;top:2045px">Lucia Moreno<br>Lima, Peru</div>
<div class="abs quote-box" style="left:290px;top:1960px">Lorem ipsum dolor sit amet, consectetur adipiscing elit, sed do eiusmod tempor incididunt ut labore et dolore magna aliqua. Ut enim ad minim veniam, quis nostrud exercitation ullamco laboris nisi ut aliquip ex ea commodo consequat.</div>

<div class="abs quote-box" style="left:290px;top:2120px">Duis aute irure dolor in reprehenderit in voluptate velit esse cillum dolore eu fugiat nulla pariatur. Excepteur sint occaecat cupidatat non proident, sunt in culpa qui officia deserunt mollit anim id est laborum et dolore.</div>
<div class="abs avatar" style="left:930px;top:2105px;background:radial-gradient(circle at 50% 45%,#a4795a 0%,#d8c0a0 55%,#8b6a4c 100%)" role="img" aria-label="Round portrait of a pet host"></div>
<div class="abs author" style="left:914px;top:2190px">Pablo Ruiz<br>Quito, Ecuador</div>

<!-- Newsletter -->
<section class="abs newsletter" role="img" aria-label="Green band with a faint paw print pattern">
  <p class="newsletter-title">Stay in touch with TORVELIS for the Lastet Dog Tips !</p>
  <div class="newsletter-form">
    <div class="newsletter-input">Your email address</div>
    <div class="newsletter-btn">Subscribe</div>
  </div>
</section>

<!-- Footer -->
<div class="abs footer-deco" role="img" aria-label="Large faint paw print decoration"></div>

<div class="footer-col" style="left:140px">
  <h4>Help</h4>
  <div>Support Center</div><div>How it Works</div><div>Contact us</div><div>Coverage</div>
  <h4 class="spaced">Hosting</h4>
  <div>Hosting</div><div>Become a Sister</div><div>Your Hosting Rates</div><div>Hosting Tips</div><div>Hosting Help</div>
</div>
<div class="footer-col" style="left:325px">
  <h4>Company</h4>
  <div>About Us</div><div>Policies</div><div>Press</div><div>Blog</div><div>Customer Reviews</div><div>Our Investors</div><div>Jobs</div><div>Terms of Service</div><div>Privacy Policy</div>
</div>
<div class="footer-col" style="left:520px">
  <h4>Top cities</h4>
  <div>Lima</div><div>Santiago</div><div>Bogota</div><div>Quito</div><div>Rosario</div><div>Montevideo</div><div>Asuncion</div><div>Cordoba</div>
</div>
<div class="footer-col" style="left:710px">
  <div class="footer-small-title">Keep Me Infoted</div>
  <div class="keep-form"><div class="keep-input">Email address</div><div class="keep-btn">Go</div></div>
  <div class="footer-small-title">Follow Us By</div>
  <div class="social-list"><span></span><span></span><span></span><span></span></div>
  <div class="social-list" style="margin-top:10px"><span></span><span></span></div>
</div>

</body>
</html>
```